Velmaro App for Smart Devices IoT WiFi Electronic

Velmaro is a siren manufacturer. This application is used for the company's products that have a Wi-Fi connection and an internet connection, which can be configured and activated remotely through this application. In addition, this application is used to activate the siren at specific times for the start and end of shifts in companies and schools. Users will be siren installers and IT or HR managers.
In addition to activating motorized sirens timers, some siren models have speakers and allow you to play TTS (text to speech) audio, audio recorded by the user on the phone and upload audio (mp3) with playlist programming with start and end times.
Application screens: home with dashboard (one dashboard for each category). Device categories: timers, speakers, motorized siren. Screen for requesting evaluation in the Play Store. Screen for registering the user profile. Screen for registering devices according to their category (timers, speakers, motorized siren). Screen for registering device groups. Screen for pairing the device on the client's Wi-Fi network. Screen for registering activation times. Screen for uploading MP3 audios. Screen for registering playlists with audio selection, start and end times. Screen for recording audio for later sending to the speakers. Screen for converting text to speech and sending to the speakers. It is important to have a time picker with the day of the week to program the activation times and playlist.

Target Market(s)

Schools, Companies and Stores.

Industry/Entity Type

IoT

Font styles to use
Sans Serif
Other font styles liked:
• roboto

Colors
FFC000
F8CF3A
FAE287
FDF2CF
FEFAEE

Requirements
Must have
• time picker with weekdays for timer programming feature.
Nice to have
• app review request screen on play store

```html
<!DOCTYPE html>
<html lang="en">
<head>
<meta charset="utf-8">
<title>Velmaro – Signup</title>
<link href="https://fonts.googleapis.com/css2?family=Poppins:ital,wght@0,400;0,500;0,600;1,800&display=swap" rel="stylesheet">
<style>
  :root {
    --amber: #f7bd00;
    --amber-deep: #f2b300;
    --paper: #ffffff;
    --screen: #f7f8fa;
    --ink: #4a5568;
    --ink-soft: #a9b0bb;
    --line: #e3e6ea;
    --ghost: #eeeff1;
    --slate: #4a5665;
  }
  * { box-sizing: border-box; margin: 0; padding: 0; }
  html, body { width: 677px; height: 1200px; overflow: hidden; }
  body {
    font-family: "Poppins", "Roboto", sans-serif;
    background: var(--screen);
    position: relative;
  }
  .status-bar {
    position: absolute; top: 0; left: 0; width: 677px; height: 60px;
    display: flex; justify-content: space-between; align-items: center;
    padding: 0 34px 0 54px; z-index: 3;
    font-weight: 600; font-size: 21px; color: var(--ink);
  }
  .status-icons { display: flex; gap: 8px; align-items: center; }
  .hero-disc {
    position: absolute; left: -230px; top: -120px;
    width: 940px; height: 590px; border-radius: 50%;
    background: linear-gradient(180deg, var(--amber) 0%, var(--amber-deep) 100%);
    z-index: 0;
  }
  .tab-title {
    position: absolute; top: 120px;
    font-weight: 800; font-style: italic; font-size: 112px;
    letter-spacing: -1px; line-height: 1; z-index: 1;
  }
  .tab-title--active { left: -2px; color: var(--paper); }
  .tab-title--idle { left: 518px; color: var(--ghost); }
  .form-card {
    position: absolute; left: 35px; top: 318px;
    width: 609px; height: 747px;
    background: var(--paper); border-radius: 34px;
    box-shadow: 0 30px 60px rgba(60, 70, 90, 0.12);
    z-index: 2;
  }
  .field {
    position: absolute; left: 53px; width: 503px; height: 66px;
    border: 1.5px solid var(--line); border-radius: 33px;
    display: flex; justify-content: space-between; align-items: center;
    padding: 0 36px 0 42px;
  }
  .field-value { font-weight: 600; font-size: 17px; color: var(--ink); }
  .field-value--secret { font-size: 24px; letter-spacing: 3px; padding-top: 6px; }
  .field-label {
    font-size: 14px; color: var(--ink-soft);
    display: flex; align-items: center; gap: 8px;
  }
  .submit-button {
    position: absolute; left: 297px; top: 1027px;
    width: 76px; height: 76px; border-radius: 50%;
    background: var(--amber);
    display: flex; justify-content: center; align-items: center;
    z-index: 3;
  }
  .social-bar {
    position: absolute; left: 0; bottom: 0; width: 677px; height: 43px;
    background: var(--slate); color: var(--paper);
    display: flex; justify-content: center; align-items: center; gap: 10px;
    font-weight: 500; font-size: 17px; letter-spacing: 0.3px;
  }
  .social-mark { width: 16px; height: 16px; background: var(--paper); border-radius: 2px; }
</style>
</head>
<body>
  <div class="status-bar">
    <span>9:41</span>
    <span class="status-icons">
      <svg width="22" height="14" viewBox="0 0 22 14"><rect x="0" y="9" width="4" height="5" rx="1" fill="#4a5568"/><rect x="6" y="6" width="4" height="8" rx="1" fill="#4a5568"/><rect x="12" y="3" width="4" height="11" rx="1" fill="#4a5568"/><rect x="18" y="0" width="4" height="14" rx="1" fill="#4a5568"/></svg>
      <svg width="20" height="14" viewBox="0 0 20 14"><path d="M10 13 L7 10 A4.5 4.5 0 0 1 13 10 Z" fill="#4a5568"/><path d="M4 7 A8.5 8.5 0 0 1 16 7" stroke="#4a5568" stroke-width="2.2" fill="none"/><path d="M1 4 A13 13 0 0 1 19 4" stroke="#4a5568" stroke-width="2.2" fill="none"/></svg>
      <svg width="30" height="14" viewBox="0 0 30 14"><rect x="0.8" y="0.8" width="25" height="12.4" rx="3" stroke="#4a5568" stroke-width="1.5" fill="none"/><rect x="3" y="3" width="20.5" height="8" rx="1.5" fill="#4a5568"/><rect x="27.5" y="4.5" width="2" height="5" rx="1" fill="#4a5568"/></svg>
    </span>
  </div>

  <div class="hero-disc"></div>
  <div class="tab-title tab-title--active">Signup</div>
  <div class="tab-title tab-title--idle">Log</div>

  <form class="form-card">
    <div class="field" style="top:48px"><span class="field-value">Aron</span><span class="field-label">First Name</span></div>
    <div class="field" style="top:139px"><span class="field-value">Vale</span><span class="field-label">Last Name</span></div>
    <div class="field" style="top:230px"><span class="field-value">Aronvale@mailnest.com</span><span class="field-label">Email</span></div>
    <div class="field" style="top:320px"><span class="field-value">+08 55-310-742</span><span class="field-label">Phone Number</span></div>
    <div class="field" style="top:411px"><span class="field-value">Education</span><span class="field-label">User Type
      <svg width="14" height="9" viewBox="0 0 14 9"><path d="M1 1 L7 7 L13 1" stroke="#a9b0bb" stroke-width="1.8" fill="none"/></svg></span></div>
    <div class="field" style="top:502px"><span class="field-value field-value--secret">*********</span><span class="field-label">Password
      <svg width="18" height="12" viewBox="0 0 18 12"><path d="M1 6 Q9 -3 17 6 Q9 15 1 6 Z" fill="#a9b0bb"/><circle cx="9" cy="6" r="2.6" fill="#fff"/></svg></span></div>
    <div class="field" style="top:598px"><span class="field-value field-value--secret">*********</span><span class="field-label">Confirm Password
      <svg width="18" height="12" viewBox="0 0 18 12"><path d="M1 6 Q9 -3 17 6 Q9 15 1 6 Z" fill="#a9b0bb"/><circle cx="9" cy="6" r="2.6" fill="#fff"/></svg></span></div>
  </form>

  <div class="submit-button" aria-label="Continue">
    <svg width="30" height="22" viewBox="0 0 30 22"><path d="M2 11 H27 M18 2 L27 11 L18 20" stroke="#ffffff" stroke-width="2.2" fill="none" stroke-linecap="round" stroke-linejoin="round"/></svg>
  </div>

  <div class="social-bar"><span class="social-mark"></span><span>SOCIALNEST</span></div>
</body>
</html>
```